Crafted Ember Website

Would like a website designed for my fitness and nutrition coaching company Craft Ember. I have a company logo and would like to keep the page layout clean and simple. Needs to look great on computer and mobile devices.

Target Market(s)

Target market is individuals looking to make changes in their health and nutrition with the help of an online coach.

Industry/Entity Type

Fitness

Number of Pages Required

2 page

Colors
3176b5
0355a3
85acd3
cedeed
f8fcfd
ffffff

Requirements
Must have
• The first page should have the company logo and name towards the top and below that client before and after photos scrolling or displaying in some manner. Also would like a section that states services offered and a section about myself since I am the primary coach for clients.

```html
<!DOCTYPE html>
<html lang="en">
<head>
<meta charset="utf-8">
<title>Crafted Ember – Fitness &amp; Nutrition Coaching</title>
<link rel="stylesheet" href="https://fonts.googleapis.com/css2?family=Oswald:wght@400;500&family=Roboto:wght@400;500;700&display=swap">
<style>
:root{
  --blue:#3176b5;
  --blue-deep:#0355a3;
  --blue-soft:#85acd3;
  --blue-pale:#cedeed;
  --ice:#f8fcfd;
  --white:#ffffff;
  --ink:#1d1d1d;
  --grey:#777;
  --band:#f4f4f4;
  --footer:#232323;
}
*{box-sizing:border-box;margin:0;padding:0}
html,body{width:1200px;height:2804px;overflow:hidden}
body{font-family:"Roboto",sans-serif;color:var(--ink);background:var(--white);position:relative}
.abs{position:absolute}
.display{font-family:"Oswald",sans-serif;font-weight:500}

/* header */
.site-header{position:absolute;top:0;left:0;width:1200px;height:103px;background:var(--white)}
.brand{left:200px;top:34px;display:flex;align-items:center;gap:12px}
.brand-mark{width:30px;height:30px;background:var(--blue)}
.brand-name{font-family:"Roboto",sans-serif;font-weight:700;font-size:20px;color:var(--blue-deep);letter-spacing:.5px}
.nav{left:482px;top:34px;display:flex;align-items:center;font-size:17px;font-weight:500}
.nav a{color:var(--ink);text-decoration:none;margin-right:44px}
.nav a.active{background:var(--blue);color:var(--white);padding:6px 16px;border-radius:2px}
.nav .divider{width:1px;height:24px;background:#555;margin:0 24px 0 -10px}
.nav .phone{display:flex;align-items:center;gap:12px;font-size:14px;font-weight:400}

/* hero */
.hero{top:103px;left:0;width:1200px;height:542px;background:linear-gradient(120deg,#3d3128 0%,#2a241f 40%,#1c1a18 100%)}
.hero-photo{position:absolute;inset:0;background:radial-gradient(circle at 22% 40%,rgba(120,70,50,.55),transparent 45%),radial-gradient(circle at 80% 70%,rgba(40,40,40,.5),transparent 50%)}
.hero-dots{left:131px;top:195px;display:flex;flex-direction:column;gap:8px}
.hero-dots span{width:10px;height:10px;border-radius:50%;background:var(--white)}
.hero-dots span:first-child{background:var(--blue)}
.hero-title{left:200px;top:165px;font-size:41px;line-height:56px;color:var(--white)}
.btn{display:flex;align-items:center;justify-content:center;color:var(--white);text-decoration:none}
.hero-cta{left:200px;top:308px;width:185px;height:47px;background:var(--blue);font-family:"Oswald",sans-serif;font-size:21px}
.ba-label{font-family:"Oswald",sans-serif;font-weight:500;font-size:18px;color:var(--white)}
.ba-circle{border-radius:50%;border:4px solid var(--blue);background:linear-gradient(180deg,#f3f3f3,#dcdcdc)}

/* sections */
.eyebrow{font-family:"Oswald",sans-serif;font-size:14px;color:var(--blue)}
.center{left:0;width:1200px;text-align:center}
.section-title{font-family:"Oswald",sans-serif;font-weight:500;font-size:38px;color:var(--ink)}
.lede{left:270px;width:660px;text-align:center;font-size:13.5px;line-height:21px;color:#555}

.services{top:645px;left:0;width:1200px;height:533px;background:var(--band)}
.card{width:184px;height:206px;top:226px;background:var(--white);border:1px dashed var(--blue);text-align:center}
.card svg{margin-top:30px}
.card h3{font-size:14.5px;font-weight:700;margin-top:18px}
.card .rule{width:46px;height:2px;background:#333;margin:12px auto}
.card p{font-size:12px;line-height:20px;color:#888;padding:0 26px}
.pager{top:470px;left:0;width:1200px;display:flex;justify-content:center;align-items:center;gap:10px}
.pager span{width:9px;height:9px;border-radius:50%;background:var(--blue)}
.pager span.on{width:18px;height:18px;border:2px solid var(--blue);background:radial-gradient(circle,var(--blue) 35%,var(--white) 40%)}

.about-photo{left:200px;top:1240px;width:337px;height:331px;background:linear-gradient(160deg,#6b7a52 0%,#4d5a37 35%,#8a5a32 70%,#6a4022 100%)}
.about-eyebrow{left:598px;top:1266px;display:flex;align-items:center;gap:16px}
.about-eyebrow .bar{width:134px;height:2px;background:var(--blue-pale);position:relative}
.about-eyebrow .bar::before{content:"";position:absolute;left:0;top:0;width:70px;height:2px;background:var(--blue)}
.about-title{left:598px;top:1298px;font-size:38px}
.about-quote{left:598px;top:1355px;width:370px;font-size:18px;font-weight:500;line-height:26px}
.about-text{left:598px;top:1425px;width:400px;font-size:12.5px;line-height:20px;color:#666}
.socials{left:600px;top:1502px;display:flex;gap:10px}
.socials span{width:41px;height:41px;background:var(--blue-pale)}

.consult{top:1638px;left:0;width:1200px;height:412px;background:linear-gradient(100deg,#1b1d20 0%,#2b2d30 45%,#3a3835 75%,#26282b 100%)}
.consult-title{top:104px;font-size:38px;color:var(--white)}
.consult-text{left:245px;width:710px;top:185px;text-align:center;font-size:14px;line-height:22px;color:#bbb}
.consult-cta{left:495px;top:297px;width:210px;height:60px;border:2px solid var(--blue);font-size:16px;font-weight:500;gap:14px}

.quote-card{top:2285px;width:361px;height:105px;background:var(--ice)}
.quote-card p{position:absolute;left:52px;top:18px;width:290px;font-size:12px;line-height:20px;color:#555}
.qmark{left:-2px;top:-8px}
.author{display:flex;align-items:center;gap:12px}
.avatar{width:46px;height:46px;border-radius:50%;border:2px solid var(--blue);background:var(--blue-pale)}
.author b{display:block;font-size:10.5px;font-weight:700}
.author small{font-size:11px;color:#666}

.site-footer{top:2512px;left:0;width:1200px;height:292px;background:var(--footer);color:#ddd}
.site-footer h4{font-family:"Roboto",sans-serif;font-weight:500;font-size:15px;color:#eee;position:absolute;top:46px}
.site-footer .col{position:absolute;top:85px;font-size:12.5px;line-height:24px}
.footer-brand{font-size:19px!important}
.newsletter-input{left:832px;top:80px;width:168px;height:34px;background:var(--white);color:#aaa;font-size:11px;padding:10px 12px}
.newsletter-send{left:832px;top:124px;width:90px;height:34px;background:var(--blue-deep);font-size:12px;font-weight:700}
.footer-rule{left:200px;top:251px;width:800px;height:1px;background:#444}
.copyright{left:200px;top:278px;font-size:11px;color:#ccc}
.footer-social{left:856px;top:268px;display:flex;gap:10px}
.footer-social span{width:28px;height:28px;border-radius:50%;background:#111}
</style>
</head>
<body>

<header class="site-header">
  <div class="abs brand"><span class="brand-mark"></span><span class="brand-name">Crafted Ember</span></div>
  <nav class="abs nav">
    <a class="active" href="#">Home</a>
    <a href="#">Consulting</a>
    <a href="#">Testimonials</a>
    <span class="divider"></span>
    <span class="phone">
      <svg width="26" height="26" viewBox="0 0 26 26"><circle cx="13" cy="13" r="12" fill="none" stroke="#3176b5" stroke-width="2"/><path d="M9 7l3 3-2 2c1 2 2 3 4 4l2-2 3 3-2 2c-5 0-10-5-10-10z" fill="#3176b5"/></svg>
      +1 555 010 2040
    </span>
  </nav>
</header>

<section class="abs hero">
  <div class="hero-photo" role="img" aria-label="Dark wooden table with a heart-shaped bowl of grains, fruit, hand grips and a skipping rope"></div>
  <div class="abs hero-dots"><span></span><span></span><span></span></div>
  <h1 class="abs hero-title display">Let Me Help You Find The Right<br>Program For Your Goals</h1>
  <a class="abs btn hero-cta" href="#">CONTACT US</a>
  <span class="abs ba-label" style="left:730px;top:110px">BEFORE</span>
  <div class="abs ba-circle" style="left:748px;top:124px;width:240px;height:240px" role="img" aria-label="Client photo before the program"></div>
  <span class="abs ba-label" style="left:1040px;top:262px">AFTER</span>
  <div class="abs ba-circle" style="left:874px;top:282px;width:202px;height:202px" role="img" aria-label="Client photo after the program"></div>
</section>

<section class="abs services">
  <div class="abs center eyebrow" style="top:56px">My Fitness and Nutrition</div>
  <h2 class="abs center section-title" style="top:80px">Our Services</h2>
  <p class="abs lede" style="top:140px">Lorem Ipsum is simply dummy text of the printing and typesetting industry. Lorem Ipsum has been the industry's standard dummy text ever since the 1500s, when an unknown printer took a galley of type</p>

  <div class="abs card" style="left:200px">
    <svg width="40" height="40" viewBox="0 0 40 40" fill="#0355a3"><rect x="2" y="16" width="4" height="8"/><rect x="7" y="10" width="5" height="20"/><rect x="12" y="18" width="16" height="4"/><rect x="28" y="10" width="5" height="20"/><rect x="34" y="16" width="4" height="8"/></svg>
    <h3>Lorem Lpsum Text</h3><div class="rule"></div>
    <p>Lorem Ipsum is simpldummy text of the printing..</p>
  </div>
  <div class="abs card" style="left:405px">
    <svg width="40" height="40" viewBox="0 0 40 40" fill="none" stroke="#0355a3" stroke-width="2.5"><path d="M20 12c-6-4-14-1-14 9s7 15 14 13c7 2 14-3 14-13s-8-13-14-9z"/><path d="M20 12c0-4 2-6 5-8"/></svg>
    <h3>Lorem Lpsum Text</h3><div class="rule"></div>
    <p>Lorem Ipsum is simpldummy text of the printing..</p>
  </div>
  <div class="abs card" style="left:610px">
    <svg width="40" height="40" viewBox="0 0 40 40" fill="#0355a3"><circle cx="22" cy="7" r="4"/><path d="M19 13h6l-2 10 5 9h-4l-4-7-4 7h-4l5-10z"/><rect x="6" y="34" width="28" height="3"/><rect x="30" y="16" width="3" height="18"/></svg>
    <h3>Lorem Lpsum Text</h3><div class="rule"></div>
    <p>Lorem Ipsum is simpldummy text of the printing..</p>
  </div>
  <div class="abs card" style="left:815px">
    <svg width="40" height="40" viewBox="0 0 40 40" fill="#0355a3"><circle cx="14" cy="8" r="4"/><rect x="9" y="14" width="10" height="14"/><rect x="10" y="28" width="3" height="9"/><rect x="15" y="28" width="3" height="9"/><path d="M22 34l8-16 8 16z" fill="none" stroke="#0355a3" stroke-width="2.5"/></svg>
    <h3>Lorem Lpsum Text</h3><div class="rule"></div>
    <p>Lorem Ipsum is simpldummy text of the printing..</p>
  </div>
  <div class="abs pager"><span class="on"></span><span></span><span></span><span></span></div>
</section>

<section class="about">
  <div class="abs about-photo" role="img" aria-label="Dumbbells, tape measure, water bottle and fresh vegetables on a wooden table"></div>
  <div class="abs about-eyebrow"><span class="eyebrow">a few words about me</span><span class="bar"></span></div>
  <h2 class="abs about-title display">About Me</h2>
  <p class="abs about-quote">“I am the Primary Coach for Clients Lorem Ipsum dummy Text”</p>
  <p class="abs about-text">Lorem Ipsum is simply dummy text of the printing and typesettingindus-try. Lorem Ipsum has been the industry's standard dummy text eversince the 1500s, when an unknown printer took a galley.....</p>
  <div class="abs socials" aria-label="Social profiles"><span></span><span></span><span></span><span></span></div>
</section>

<section class="abs consult" role="img" aria-label="Dim gym with people doing push-ups" style="">
  <svg class="abs" style="left:560px;top:46px" width="80" height="44" viewBox="0 0 80 44" fill="#3176b5"><rect x="4" y="6" width="6" height="16"/><rect x="12" y="2" width="6" height="24"/><rect x="18" y="12" width="44" height="4"/><rect x="62" y="2" width="6" height="24"/><rect x="70" y="6" width="6" height="16"/><circle cx="40" cy="24" r="5"/><path d="M32 16l4 14h8l4-14-3 0-3 8h-4l-3-8z"/><rect x="35" y="30" width="10" height="12"/></svg>
  <h2 class="abs center consult-title display">Consulting</h2>
  <p class="abs consult-text">Lorem Ipsum is simply dummy text of the printing and typesetting industry. Lorem Ipsum has been the industry's standard dummy text ever since the 1500s, when an unknown printer took a galley of type and scrambled it to make a type specimen book.</p>
  <a class="abs btn consult-cta" href="#">
    <svg width="20" height="20" viewBox="0 0 20 20"><path d="M3 2l4 4-2 3c1 2 3 4 6 6l3-2 4 4-3 3C8 20 0 12 0 5z" fill="#3176b5"/></svg>
    CONTACT US
  </a>
</section>

<section class="testimonials">
  <div class="abs center eyebrow" style="top:2105px">My Fitness and Nutrition</div>
  <h2 class="abs center section-title" style="top:2128px">testimonials</h2>
  <p class="abs lede" style="top:2188px">Lorem Ipsum is simply dummy text of the printing and typesetting industry. Lorem Ipsum has been the industry's standard dummy text ever since the 1500s, when an unknown printer took a galley of type</p>

  <div class="abs quote-card" style="left:200px">
    <svg class="abs qmark" width="36" height="28" viewBox="0 0 36 28" fill="#3176b5"><path d="M0 12h8l-4 14H0zM2 12c0-7 3-11 8-12v4c-3 1-4 4-4 8zM18 12h8l-4 14h-4zM20 12c0-7 3-11 8-12v4c-3 1-4 4-4 8z"/></svg>
    <p>Lorem Ipsum is simply dummy text of the printing and typesetting industry. Lorem Ipsum has been theindus-try's standard dummy text ever since the text..</p>
  </div>
  <div class="abs author" style="left:359px;top:2406px"><span class="avatar" role="img" aria-label="Client portrait"></span><span><b>DANA WHITLOW</b><small>23 Oct, 2017</small></span></div>

  <div class="abs quote-card" style="left:639px">
    <svg class="abs qmark" width="36" height="28" viewBox="0 0 36 28" fill="#3176b5"><path d="M0 12h8l-4 14H0zM2 12c0-7 3-11 8-12v4c-3 1-4 4-4 8zM18 12h8l-4 14h-4zM20 12c0-7 3-11 8-12v4c-3 1-4 4-4 8z"/></svg>
    <p>Lorem Ipsum is simply dummy text of the printing and typesetting industry. Lorem Ipsum has been theindus-try's standard dummy text ever since the text..</p>
  </div>
  <div class="abs author" style="left:798px;top:2406px"><span class="avatar" role="img" aria-label="Client portrait"></span><span><b>MARCO REYES</b><small>23 Oct, 2017</small></span></div>
</section>

<footer class="abs site-footer">
  <h4 class="footer-brand" style="left:200px">Crafted Ember</h4>
  <p class="col" style="left:200px;width:210px;font-size:12.5px;line-height:24px">Lorem Ipsum is simply dummy text of the printing and typesetting industry. Lorem Ipsum has been the industry's standard dummy text ever since the 1500s, when an unknown printer took a galley of text....</p>
  <h4 style="left:454px">Quick Links</h4>
  <div class="col" style="left:454px">Home<br>Consulting<br>Testimonials<br>Services<br>Help</div>
  <h4 style="left:587px">My Contacts</h4>
  <div class="col" style="left:587px">Phone :&nbsp;&nbsp;&nbsp;+1 555 010 2040<br>E-mail :&nbsp;&nbsp;info@craftedember.com<br>Address :&nbsp;&nbsp;lorem ipsum dummy text<br><span style="padding-left:64px">printer gallary..</span></div>
  <h4 style="left:832px">NEWSLETTER</h4>
  <div class="abs newsletter-input">your email address</div>
  <div class="abs btn newsletter-send">SEND</div>
  <div class="abs footer-rule"></div>
  <div class="abs copyright">© 2016 Crafted Ember. All rights reserved.</div>
  <div class="abs footer-social" aria-label="Social profiles"><span></span><span></span><span></span><span></span></div>
</footer>

</body>
</html>
```